Design for three pages of a 12-page 4-color 8.5 x 11 magazine-type booklet

We will be taking the information from a webpage at glowmerestudies.org and putting it into a 12-page 4-color 8.5 x 11 magazine-type booklet that will look like an upscale company report. I need to have a design in Photoshop for the cover and two inside pages that I can use as the template for the pages. I likely will also need help putting it together once I start putting the contents into the pages. I may just decide on the content and have the designer create the booklet as an additional freelance contract. First, I need a design for (1) the front cover, (2) one information page taken from information on http://www.glowmerestudies.org/kvon-project-management-staff/, and (3) one of the pages that has a researcher from this page on it: http://www.glowmerestudies.org/teaching-people-how-to-have/. That's designs for three pages. The designs have to be very professional looking and businesslike. We will be using the booklet to pitch to foundations and philanthropists. The work on the publication itself would be additional freelance work on an hourly basis.

Serif

• Professional look

```html
<!DOCTYPE html>
<html lang="en">
<head>
<meta charset="utf-8">
<title>KVON Booklet – Front Page</title>
<link href="https://fonts.googleapis.com/css2?family=Exo+2:wght@400;500;700&display=swap" rel="stylesheet">
<style>
  :root {
    --stage: #474747;
    --navy: #232a66;
    --navy-deep: #120f3a;
    --blue: #0a5aa8;
    --ink: #111111;
    --rule: #6a6a6a;
    --mark-grey: #666666;
    --caption: #ffffff;
  }
  * { box-sizing: border-box; margin: 0; padding: 0; }
  html, body {
    width: 1200px; height: 1200px; overflow: hidden;
    background: var(--stage);
    font-family: "Exo 2", sans-serif;
  }
  .canvas { position: relative; width: 1200px; height: 1200px; }
  .cover {
    position: absolute; left: 203px; top: 62px;
    width: 794px; height: 1027px; overflow: hidden;
    background: linear-gradient(172deg, #ffffff 0%, #f3f3f3 30%, #cfcfcf 62%, #9a9a9a 85%, #6c6c6c 100%);
  }
  .brand {
    position: absolute; left: 112px; top: 170px; width: 270px;
  }
  .brand-name {
    display: flex; align-items: center; gap: 12px;
    font-weight: 700; font-size: 66px; line-height: 1;
    color: var(--navy); letter-spacing: 1px;
  }
  .brand-square { width: 22px; height: 22px; background: var(--mark-grey); }
  .brand-full {
    margin-top: 14px; font-size: 11.5px; font-weight: 500;
    color: var(--ink); white-space: nowrap;
  }
  .divider {
    position: absolute; left: 414px; top: 113px;
    width: 1.5px; height: 174px; background: var(--rule);
  }
  .tagline {
    position: absolute; left: 459px; top: 150px;
    font-size: 41px; line-height: 37px; font-weight: 500; color: var(--ink);
  }
  .tagline .accent { color: var(--blue); }
  .base-dome {
    position: absolute; left: 0; top: 0; width: 794px; height: 1027px;
  }
  .caption {
    position: absolute; left: 0; top: 1118px; width: 100%;
    text-align: center; color: var(--caption);
    font-size: 30px; font-weight: 400; letter-spacing: 0.5px;
  }
</style>
</head>
<body>
  <div class="canvas">
    <section class="cover">
      <div class="brand">
        <div class="brand-name"><span>KVON</span><span class="brand-square"></span></div>
        <div class="brand-full">Glowmere Research and Education Institute, Inc.</div>
      </div>
      <div class="divider"></div>
      <h1 class="tagline">Bridging<br><span class="accent">Heaven</span> and<br><span class="accent">Earth</span></h1>
      <svg class="base-dome" viewBox="0 0 794 1027" aria-hidden="true">
        <defs>
          <linearGradient id="domeFill" x1="0" y1="0" x2="1" y2="1">
            <stop offset="0" stop-color="var(--navy)"/>
            <stop offset="1" stop-color="var(--navy-deep)"/>
          </linearGradient>
        </defs>
        <path d="M0 1027 L0 860 C0 680 190 546 397 546 C604 546 794 680 794 860 L794 1027 Z" fill="url(#domeFill)"/>
      </svg>
    </section>
    <p class="caption">front page</p>
  </div>
</body>
</html>
```